Potential SF Gazette Best Seller Poetry Book Cover Contest

I’m penning my first poetry book. It’s entitled “Lanterns Under Rain”
I’m fairly open to creative freedom but I want the cover to without a doubt catch a persons' eye instantly because first impressions are VERY IMPORTANT in the literary world
I tend to lean towards a luxury look and colors like black, gold, rose gold, silver, glitter etc but again I’m open to interpretation
Looking forward to your submissions
Target Market(s)
those seeking relatable love advice and quotes
modern millenials
Colors
Look and feel

```html
<!DOCTYPE html>
<html lang="en">
<head>
<meta charset="utf-8">
<title>Lanterns Under Rain — Book Cover</title>
<link href="https://fonts.googleapis.com/css2?family=Jim+Nightshade&display=swap" rel="stylesheet">
<style>
  :root {
    --blush: #f1cdb9;
    --peach: #f4c8a6;
    --rose: #e8b9ab;
    --gold-glow: rgba(255, 214, 70, 0.75);
    --gold-soft: rgba(255, 220, 100, 0.45);
    --gold: #f9c41e;
    --gold-deep: #f0ac12;
    --gold-light: #ffe27a;
    --ink: #141110;
  }
  html, body {
    margin: 0;
    padding: 0;
    overflow: hidden;
    background: var(--blush);
  }
  .cover {
    position: relative;
    width: 774px;
    height: 1200px;
    overflow: hidden;
    font-family: "Jim Nightshade", cursive;
    color: var(--ink);
  }
  .glitter-backdrop {
    position: absolute;
    inset: 0;
    background:
      radial-gradient(circle at 8% 70%, var(--gold-glow) 0%, rgba(255,214,70,0) 14%),
      radial-gradient(circle at 22% 93%, var(--gold-soft) 0%, rgba(255,214,70,0) 16%),
      radial-gradient(circle at 90% 12%, var(--gold-soft) 0%, rgba(255,214,70,0) 18%),
      radial-gradient(circle at 75% 26%, var(--gold-soft) 0%, rgba(255,214,70,0) 14%),
      radial-gradient(circle at 10% 14%, var(--gold-soft) 0%, rgba(255,214,70,0) 16%),
      radial-gradient(circle at 95% 88%, var(--gold-soft) 0%, rgba(255,214,70,0) 16%),
      radial-gradient(circle at 60% 82%, rgba(120,100,110,0.25) 0%, rgba(120,100,110,0) 14%),
      radial-gradient(circle at 20% 36%, rgba(120,100,110,0.18) 0%, rgba(120,100,110,0) 14%),
      linear-gradient(180deg, var(--blush) 0%, var(--peach) 50%, var(--rose) 100%);
  }
  .heart-art {
    position: absolute;
    left: 30px;
    top: 370px;
    width: 714px;
    height: 620px;
    background:
      radial-gradient(ellipse at 50% 45%, var(--gold-light) 0%, var(--gold) 40%, var(--gold-deep) 58%, rgba(240,172,18,0.5) 66%, rgba(240,172,18,0) 74%);
  }
  .series-label {
    position: absolute;
    left: 0;
    width: 774px;
    text-align: center;
    margin: 0;
    font-weight: 400;
    white-space: nowrap;
    line-height: 1;
  }
  .genre {
    top: 96px;
    font-size: 32px;
    letter-spacing: 0.2em;
  }
  .tagline {
    top: 140px;
    font-size: 34px;
    letter-spacing: 0.16em;
  }
  .title {
    position: absolute;
    top: 455px;
    left: 0;
    width: 774px;
    margin: 0;
    text-align: center;
    font-weight: 400;
    font-size: 140px;
    line-height: 146px;
  }
  .title span { display: block; }
  .author {
    position: absolute;
    top: 1100px;
    left: 0;
    width: 774px;
    margin: 0;
    text-align: center;
    font-size: 52px;
    line-height: 1;
    letter-spacing: 0.16em;
    white-space: nowrap;
  }
</style>
</head>
<body>
  <main class="cover">
    <div class="glitter-backdrop" role="img" aria-label="Soft blush background with swirling strands of golden glitter and bokeh lights"></div>
    <div class="heart-art" role="img" aria-label="Large glittering gold heart illustration covered in sparkling beads"></div>

    <p class="series-label genre">Poetry</p>
    <p class="series-label tagline">Reliable Love Advice and Quotes</p>

    <h1 class="title">
      <span>Lanterns</span>
      <span>Under</span>
      <span>Rain</span>
    </h1>

    <p class="author">Morgan Ashby-Vale</p>
  </main>
</body>
</html>
```